ARC VOLLEY Business Card Project

I'd like to request a business card design for the new company I've launched.
The name of the company is "ARC VOLLEY" an indoor unmanned tennis practice facility.
We would like to see designs that use our brand identity color in the logo I've attached.
We hope to get the design with modern, luxurious and elegant tone and manner.
We hope the logo should not be too big.

Business card must have elements as below:
- Logo (One of the logos I've attached)
- Name (In Korean Text) : 박 서 윤
- Title (In Korean Text) : 대표
- Phone Number : 010-8472-3916
- Email Address : seoyun.park@arcvolley-example.co.kr
- Website : www.arcvolley-example.co.kr
- Instagram : arcvolley
- Address (In Korean text) : 경기도 용인시 수지구 풍덕천로 456 미래타워 5층 501호, 502호

Target Market(s)

Tennis amateurs in 20 to 40s

Industry/Entity Type

Sports, Hobby

Contact Information for Business Card

- Logo (One of the logos I've attached) - Name (In Korean Text) : 박 서 윤 - Title (In Korean Text) : 대표 - Phone Number : 010-8472-3916 - Email Address : seoyun.park@arcvolley-example.co.kr - Website : www.arcvolley-example.co.kr - Instagram : arcvolley - Address (In Korean text) : 경기도 용인시 수지구 풍덕천로 456 미래타워 5층 501호, 502호

Font styles to use
Sans Serif

Requirements
Must have
• Double sided
Nice to have
• Logo with intaglio or relief embossing
Should not have
• Logo should not be too big.

```html
<!DOCTYPE html>
<html lang="ko">
<head>
<meta charset="utf-8">
<title>ARC VOLLEY Business Card</title>
<link rel="stylesheet" href="https://fonts.googleapis.com/css2?family=EB+Garamond:wght@500&family=Noto+Serif+KR:wght@400;700&display=swap">
<style>
  :root {
    --backdrop: #2a2a2a;
    --card-green: #2c5535;
    --card-green-light: #34633f;
    --card-white: #f2f2f1;
    --brand-green: #1f4a2b;
    --mark-green: #3a6d45;
    --silver: #d6d8d5;
    --ink: #444444;
  }
  * { margin: 0; padding: 0; box-sizing: border-box; }
  html, body {
    width: 1200px; height: 1138px; overflow: hidden;
    background: var(--backdrop);
  }
  .card {
    position: absolute;
    left: 275px;
    width: 620px;
    height: 375px;
    border-radius: 16px;
  }
  .card-front {
    top: 186px;
    background: radial-gradient(ellipse at 50% 40%, var(--card-green-light), var(--card-green));
  }
  .card-back {
    top: 608px;
    background: var(--card-white);
  }
  .brand-mark {
    position: absolute;
    border-radius: 50%;
  }
  .card-front .brand-mark {
    left: 240px; top: 80px; width: 138px; height: 138px;
    background: var(--mark-green);
  }
  .card-back .brand-mark {
    left: 32px; top: 42px; width: 90px; height: 90px;
    background: var(--brand-green);
  }
  .brand-name {
    position: absolute;
    font-family: "EB Garamond", serif;
    font-weight: 500;
    letter-spacing: 1px;
    white-space: nowrap;
  }
  .card-front .brand-name {
    left: 0; right: 0; top: 226px;
    text-align: center;
    font-size: 44px;
    color: var(--silver);
  }
  .card-back .brand-name {
    left: 158px; top: 56px;
    font-size: 44px;
    color: var(--brand-green);
  }
  .person-name {
    position: absolute; left: 35px; top: 200px;
    font-family: "Noto Serif KR", serif;
    font-weight: 700; font-size: 29px;
    color: var(--brand-green);
    letter-spacing: 2px;
  }
  .person-title {
    position: absolute; left: 36px; top: 244px;
    font-family: "Noto Serif KR", serif;
    font-weight: 700; font-size: 13px;
    color: #333;
  }
  .contact {
    position: absolute;
    display: flex; align-items: center; gap: 8px;
    font-family: "Noto Serif KR", serif;
    font-size: 14.5px;
    color: var(--ink);
    white-space: nowrap;
  }
  .contact svg { width: 14px; height: 14px; flex: none; }
  .c-phone { left: 36px; top: 281px; }
  .c-web { left: 175px; top: 281px; }
  .c-insta { left: 36px; top: 305px; }
  .c-mail { left: 175px; top: 305px; }
  .c-addr { left: 36px; top: 329px; }
</style>
</head>
<body>
  <section class="card card-front">
    <div class="brand-mark"></div>
    <div class="brand-name">ARC VOLLEY</div>
  </section>

  <section class="card card-back">
    <div class="brand-mark"></div>
    <div class="brand-name">ARC VOLLEY</div>

    <div class="person-name">박 서 윤</div>
    <div class="person-title">대표</div>

    <div class="contact c-phone">
      <svg viewBox="0 0 16 16" aria-hidden="true"><path fill="#1f4a2b" d="M2 5c0-2 2-3 6-3s6 1 6 3v1h-3V5H5v1H2zM4 7h8l2 6H2z"/></svg>
      <span>010-8472-3916</span>
    </div>
    <div class="contact c-web">
      <svg viewBox="0 0 16 16" aria-hidden="true"><rect x="1" y="3" width="14" height="10" fill="#1f4a2b"/><path d="M1 3l7 6 7-6" stroke="#f2f2f1" stroke-width="1.4" fill="none"/></svg>
      <span>www.arcvolley-example.co.kr</span>
    </div>
    <div class="contact c-insta">
      <svg viewBox="0 0 16 16" aria-hidden="true"><rect x="2" y="2" width="12" height="12" rx="3" fill="none" stroke="#1f4a2b" stroke-width="1.6"/></svg>
      <span>#arcvolley</span>
    </div>
    <div class="contact c-mail">
      <svg viewBox="0 0 16 16" aria-hidden="true"><circle cx="8" cy="8" r="6" fill="none" stroke="#1f4a2b" stroke-width="1.4"/><path d="M2 8h12M8 2c-3 3-3 9 0 12M8 2c3 3 3 9 0 12" stroke="#1f4a2b" stroke-width="1.2" fill="none"/></svg>
      <span>seoyun.park@arcvolley-example.co.kr</span>
    </div>
    <div class="contact c-addr">
      <svg viewBox="0 0 16 16" aria-hidden="true"><path fill="#1f4a2b" d="M8 1a5 5 0 0 0-5 5c0 4 5 9 5 9s5-5 5-9a5 5 0 0 0-5-5zm0 7a2 2 0 1 1 0-4 2 2 0 0 1 0 4z"/></svg>
      <span>경기도 용인시 수지구 풍덕천로 456 미래타워 5층 501호, 502호</span>
    </div>
  </section>
</body>
</html>
```